Wordpress theme website for professionals working together

My partner and I are offering business services, my wife in the energy business as mainly as member of the board of commissioners. I am working as interim manager/consultant in the accounting and finance area. Both activities are connected in one company VELMORO BV (dutch ltd). We need a CV based website. Beside this we do some financial and accounting services.

Target Market(s)

small medium business

Font styles to use
Sans Serif

Colors

Designer to choose colors to be used in the design.

Requirements
Must have
• Pictures of both members.
• CLEAN AND SIMPLE
• I LIKE BLACK & WHITE
Nice to have
• I like design like this theme: http://theme.brindlepax.com/resume/

```html
<!DOCTYPE html>
<html lang="en">
<head>
<meta charset="utf-8">
<title>VELMORO BV – Contact</title>
<link rel="stylesheet" href="https://fonts.googleapis.com/css2?family=Lato:wght@400;700;900&display=swap">
<style>
  :root {
    --ink: #111111;
    --text: #222222;
    --muted: #555555;
    --band: #f1f1f1;
    --white: #ffffff;
    --field-border: #c9c9c9;
    --button: #212121;
    --brand-blue: #10305f;
    --brand-red: #b8000a;
  }
  * { box-sizing: border-box; margin: 0; padding: 0; }
  html, body { width: 1200px; height: 676px; overflow: hidden; }
  body {
    font-family: "Lato", Arial, sans-serif;
    color: var(--text);
    background: var(--white);
    position: relative;
  }
  .site-header {
    height: 109px;
    display: flex;
    align-items: center;
    justify-content: space-between;
    padding: 0 74px;
  }
  .brand {
    display: flex;
    align-items: center;
    gap: 10px;
    font-weight: 900;
    font-size: 34px;
    letter-spacing: 0.5px;
    color: var(--brand-blue);
    margin-top: 6px;
  }
  .brand-mark {
    width: 14px; height: 14px;
    background: var(--brand-red);
  }
  .main-nav, .footer-nav {
    display: flex;
    list-style: none;
    font-size: 13px;
    text-transform: uppercase;
    letter-spacing: 0.2px;
  }
  .main-nav { gap: 34px; margin-top: 2px; }
  .main-nav li.is-active { font-weight: 700; color: var(--ink); }
  .contact-band {
    height: 401px;
    background: var(--band);
    padding-top: 46px;
  }
  .contact-title {
    text-align: center;
    font-weight: 900;
    font-size: 33px;
    color: var(--ink);
    letter-spacing: 0.3px;
    line-height: 1;
  }
  .contact-form {
    width: 693px;
    margin: 34px auto 0;
  }
  .field-row { display: flex; justify-content: space-between; }
  .field {
    background: var(--white);
    border: 1px solid var(--field-border);
    border-radius: 2px;
    font-size: 13px;
    color: var(--ink);
    padding: 13px 13px;
  }
  .field-short { width: 333px; height: 41px; }
  .field-message { width: 692px; height: 123px; margin-top: 8px; }
  .form-actions {
    display: flex;
    justify-content: center;
    gap: 13px;
    margin-top: 18px;
    padding-right: 4px;
  }
  .button {
    height: 49px;
    background: var(--button);
    color: var(--white);
    font-weight: 700;
    font-size: 18px;
    display: flex;
    align-items: center;
    justify-content: center;
    border-radius: 2px;
  }
  .button-submit { width: 208px; }
  .button-request { width: 281px; }
  .site-footer { text-align: center; padding-top: 49px; }
  .footer-nav { justify-content: center; gap: 34px; }
  .copyright { font-size: 13px; color: var(--muted); margin-top: 21px; }
  .social-links {
    display: flex;
    justify-content: center;
    gap: 21px;
    margin-top: 20px;
    list-style: none;
  }
  .social-links li {
    width: 20px; height: 20px;
    border-radius: 50%;
    background: var(--muted);
  }
</style>
</head>
<body>
  <header class="site-header">
    <div class="brand"><span>VELMORO</span><span class="brand-mark"></span></div>
    <ul class="main-nav">
      <li class="is-active">Home</li>
      <li>Actual Jobs</li>
      <li>Finished Jobs</li>
      <li>Skills</li>
      <li>Education</li>
      <li>Contact</li>
      <li>More...</li>
    </ul>
  </header>

  <section class="contact-band">
    <h1 class="contact-title">CONTACT US</h1>
    <div class="contact-form">
      <div class="field-row">
        <div class="field field-short">Name</div>
        <div class="field field-short">Email Address</div>
      </div>
      <div class="field field-message">Message</div>
      <div class="form-actions">
        <div class="button button-submit">SUBMIT</div>
        <div class="button button-request">REQUEST FOR INFORMATION</div>
      </div>
    </div>
  </section>

  <footer class="site-footer">
    <ul class="footer-nav">
      <li>Home</li>
      <li>Actual Jobs</li>
      <li>Finished Jobs</li>
      <li>Skills</li>
      <li>Education</li>
      <li>Contact</li>
      <li>More...</li>
    </ul>
    <p class="copyright">Copyright© 2018 Company Name. All Right Reserved</p>
    <ul class="social-links" aria-label="Social links">
      <li></li><li></li><li></li><li></li><li></li>
    </ul>
  </footer>
</body>
</html>
```